Bref créative
Fire sprinkler company stationary
Halbrook Automatic Sprinkler Co.
Simple
Trent Okafor
President
2745 Pelling Street, Knoxville, TN 37921
contact@halbrooksprinkler.example
The logo to use on the stationary.

```html
<!DOCTYPE html>
<html lang="en">
<head>
<meta charset="utf-8">
<title>Halbrook Automatic Sprinkler Co. — Business Card</title>
<link rel="stylesheet" href="https://fonts.googleapis.com/css2?family=Archivo+Black&family=Oswald:wght@500&family=Open+Sans:wght@400;600&display=swap">
<style>
  :root {
    --page: #e9e9ea;
    --card: #ffffff;
    --ink: #1c1c1c;
    --muted: #6b6b6b;
    --gold: #b8891f;
    --gold-light: #d9b04a;
    --black: #111111;
  }
  * { box-sizing: border-box; margin: 0; padding: 0; }
  html, body { width: 1200px; height: 864px; overflow: hidden; }
  body {
    background: var(--page);
    font-family: "Open Sans", sans-serif;
    color: var(--ink);
    position: relative;
  }
  .card {
    position: absolute;
    left: 270px;
    width: 660px;
    height: 377px;
    background: var(--card);
    border-radius: 26px;
    overflow: hidden;
    box-shadow: 0 6px 18px rgba(0,0,0,0.12);
  }
  .card--back { top: 36px; }
  .card--front { top: 451px; }

  .brand-mark {
    display: flex;
    align-items: center;
    gap: 8px;
    font-family: "Open Sans", sans-serif;
    font-weight: 600;
    color: var(--ink);
  }
  .brand-mark__dot {
    border-radius: 50%;
    background: var(--gold);
  }

  /* back */
  .card--back .brand-mark {
    position: absolute;
    left: 50%; top: 140px;
    transform: translateX(-50%);
    font-size: 30px;
  }
  .card--back .brand-mark__dot { width: 40px; height: 40px; }
  .back-web {
    position: absolute;
    left: 0; right: 0; top: 230px;
    text-align: center;
    font-size: 11px;
    letter-spacing: 3px;
    text-transform: uppercase;
    color: var(--gold);
  }

  /* front */
  .card--front .brand-mark {
    position: absolute;
    left: 36px; top: 128px;
    font-size: 20px;
  }
  .card--front .brand-mark__dot { width: 30px; height: 30px; }
  .company {
    position: absolute;
    left: 190px; top: 108px;
  }
  .company__name {
    font-family: "Archivo Black", sans-serif;
    font-size: 46px;
    line-height: 1;
    letter-spacing: 0.5px;
    color: var(--black);
  }
  .company__tag {
    font-family: "Oswald", sans-serif;
    font-weight: 500;
    font-size: 21px;
    letter-spacing: 1.6px;
    color: var(--gold);
    margin-top: 4px;
  }
  .contacts {
    position: absolute;
    right: 30px; top: 30px;
    list-style: none;
    font-size: 11px;
    color: var(--muted);
  }
  .contacts li { display: flex; align-items: center; gap: 7px; margin-bottom: 6px; }
  .contacts svg { width: 14px; height: 14px; flex: none; }
  .person {
    position: absolute;
    left: 190px; top: 232px;
  }
  .person__name { font-size: 16px; font-weight: 600; color: var(--ink); }
  .person__role { font-size: 11px; letter-spacing: 2px; text-transform: uppercase; color: var(--gold); }
  .address {
    position: absolute;
    left: 36px; bottom: 26px;
    font-size: 11px;
    color: var(--muted);
  }
  .wave { position: absolute; inset: 0; width: 660px; height: 377px; }
</style>
</head>
<body>

<section class="card card--back">
  <div class="brand-mark"><span class="brand-mark__dot"></span>velmora</div>
  <p class="back-web">www.halbrooksprinkler.example</p>
</section>

<section class="card card--front">
  <svg class="wave" viewBox="0 0 660 377" aria-hidden="true">
    <path d="M330 377 C430 360 520 300 660 230 L660 377 Z" fill="var(--gold-light)"/>
    <path d="M380 377 C470 362 550 318 660 262 L660 377 Z" fill="var(--gold)"/>
    <path d="M420 377 C500 366 570 332 660 290 L660 377 Z" fill="var(--black)"/>
  </svg>

  <ul class="contacts">
    <li>
      <svg viewBox="0 0 14 14"><circle cx="7" cy="7" r="7" fill="var(--black)"/><path d="M4.6 3.8l1.3 1.3-.7.9c.5 1 1.2 1.7 2.2 2.2l.9-.7 1.3 1.3-.8 1.1C6.5 9.6 4.4 7.5 4 5l.6-1.2z" fill="#fff"/></svg>
      865 555-0142
    </li>
    <li>
      <svg viewBox="0 0 14 14"><circle cx="7" cy="7" r="7" fill="var(--black)"/><circle cx="7" cy="7" r="3.6" fill="none" stroke="#fff" stroke-width="0.9"/><path d="M3.4 7h7.2M7 3.4v7.2" stroke="#fff" stroke-width="0.8"/></svg>
      www.halbrooksprinkler.example
    </li>
    <li>
      <svg viewBox="0 0 14 14"><circle cx="7" cy="7" r="7" fill="var(--black)"/><rect x="3.5" y="4.6" width="7" height="4.8" fill="none" stroke="#fff" stroke-width="0.9"/><path d="M3.5 4.8L7 7.4l3.5-2.6" fill="none" stroke="#fff" stroke-width="0.9"/></svg>
      contact@halbrooksprinkler.example
    </li>
  </ul>

  <div class="brand-mark"><span class="brand-mark__dot"></span>velmora</div>

  <div class="company">
    <h1 class="company__name">HALBROOK</h1>
    <p class="company__tag">AUTOMATIC SPRINKLER CO.</p>
  </div>

  <div class="person">
    <p class="person__name">Trent Okafor</p>
    <p class="person__role">President</p>
  </div>

  <p class="address">2745 Pelling Street, Knoxville, TN 37921</p>
</section>

</body>
</html>
```